Stationery for Family Law Attorney
Business Cards, Envelope, Letterhead
Stationery for Family Law Attorney - Law
Creative Brief
Professional
Marisol K. Denby
Attorney & Counselor at Law
27815 E. Halvorsen Lane Suite 300 San Diego, CA 92984
marisol@counseldenby.example
Exclusively Family Law www.counseldenby.example
MDenby MDenby
Please note the address should read as follows, on the following lines: Line 1: The Quillgate Line 2: 27815 E. Halvorsen Lane Line 3: Suite 610 Line 4: San Diego, CA 92984
Please note the "San Diego, CA 92984" needs to all be on the same line. (858) 555-0147 is the fax line - not the cell. Also, please add the words "The Quillgate" on the line above the 27815 E. Halvorsen Lane line.
Vektor Vektor
sir please check you inbox top right side this web page
Re #37: Please make the back gray. Please replace the symbols with the words for the contact information (i.e. "Phone"). Please remove the website from the front.
Re #30: Please make the "Marisol K. Denby" and "Attorney & Counselor at Law part in small and large caps. Please remove the website from the front of the card. Instead of letters, please write out "Phone" "Fax" and "Email". Thanks. I really like the gray back of the card.

```html
<!DOCTYPE html>
<html lang="en">
<head>
<meta charset="utf-8">
<title>Marisol K. Denby Stationery</title>
<link href="https://fonts.googleapis.com/css2?family=Cinzel:wght@400;600&family=Open+Sans:wght@400;600&display=swap" rel="stylesheet">
<style>
:root{
  --bg:#2a2a2b;
  --paper:#ffffff;
  --paper-shade:#eef1f3;
  --blue:#1c8cc2;
  --blue-dark:#0f5f8c;
  --gray:#5b5d60;
  --gray-dark:#3f4144;
  --ink:#4a4c4f;
  --label:#9a9a9a;
}
*{box-sizing:border-box;margin:0;padding:0}
html,body{width:1200px;height:372px;overflow:hidden;background:var(--bg)}
.canvas{position:relative;width:1200px;height:372px;background:radial-gradient(ellipse at 50% 40%,#333436,var(--bg));font-family:"Open Sans",sans-serif;color:var(--ink)}
.abs{position:absolute}
.brand-name{font-family:"Cinzel",serif;font-weight:600;letter-spacing:.04em;font-variant:small-caps;white-space:nowrap}
.brand-mark{display:flex;align-items:center;gap:5px;white-space:nowrap}
.brand-square{width:9px;height:9px;background:var(--blue);flex:none}
.label{position:absolute;font-size:5px;color:var(--label);letter-spacing:.03em;white-space:nowrap}

/* identity header */
.identity{left:24px;top:26px;width:200px;color:#e8e8e8}
.identity .brand-name{font-size:15px;color:#f2f2f2}
.identity .title{font-size:6px;letter-spacing:.12em;margin-top:4px;color:#bdbdbd;text-transform:uppercase}
.identity .concept{font-size:5px;margin-top:10px;color:#8d8d8d}

/* cards */
.card{position:absolute;width:120px;height:64px;box-shadow:0 2px 4px rgba(0,0,0,.5);overflow:hidden}
.card-front{background:var(--paper);display:flex;align-items:center;justify-content:center}
.card-front .brand-name{font-size:9px;color:var(--gray-dark)}
.card-front.gray{background:linear-gradient(160deg,#6a6c6f,var(--gray-dark))}
.card-front.gray .brand-name{color:#fff}
.card-back{background:linear-gradient(180deg,#fff 0,#fff 62%,var(--blue) 62%,var(--blue-dark) 100%);padding:8px 9px}
.card-back.gray{background:linear-gradient(150deg,#6b6d70,var(--gray-dark))}
.card-back .person{font-family:"Cinzel",serif;font-size:6.5px;font-weight:600;color:var(--gray-dark);font-variant:small-caps;white-space:nowrap}
.card-back .role{font-size:3.6px;letter-spacing:.06em;color:#777;text-transform:uppercase;margin-top:1px;white-space:nowrap}
.card-back .contact{font-size:3.6px;line-height:1.35;margin-top:5px;color:#555;white-space:nowrap}
.card-back.gray .person{color:#fff}
.card-back.gray .role,.card-back.gray .contact{color:#e3e3e3}

/* letterheads */
.letterhead{position:absolute;top:29px;width:242px;height:314px;background:var(--paper);box-shadow:0 3px 6px rgba(0,0,0,.5);overflow:hidden}
.letterhead .head{position:absolute;top:10px;left:0;right:0;display:flex;justify-content:center}
.letterhead .brand-name{font-size:9px;color:var(--gray-dark)}
.letterhead .address{position:absolute;top:12px;right:14px;font-size:3.6px;line-height:1.4;color:#777;text-align:left;white-space:nowrap}
.letterhead .band{position:absolute;left:0;right:0;bottom:0;height:9px;background:linear-gradient(90deg,var(--blue-dark),var(--blue),var(--blue-dark))}
.letterhead .foot{position:absolute;left:0;right:0;bottom:13px;text-align:center;font-size:3.6px;color:#888}

/* envelopes */
.envelope{position:absolute;left:864px;width:312px;height:108px;box-shadow:0 3px 6px rgba(0,0,0,.5);overflow:hidden}
.envelope svg{position:absolute;inset:0}
.envelope .brand-mark{position:absolute}
.envelope .brand-name{font-size:8px}
.envelope .return{position:absolute;left:14px;top:10px;display:flex;flex-direction:column;align-items:flex-start;font-size:3.6px;line-height:1.4;color:#777;white-space:nowrap}
.envelope .return .brand-mark{position:static;margin-bottom:3px}
.envelope .return .brand-square{width:7px;height:7px}
.envelope .return .brand-name{font-size:6.5px;color:var(--gray-dark)}
.envelope .edge{position:absolute;left:0;right:0;bottom:0;height:6px;background:var(--blue)}
</style>
</head>
<body>
<div class="canvas">

  <header class="identity abs">
    <div class="brand-mark"><span class="brand-square"></span><span class="brand-name">Marisol K. Denby</span></div>
    <div class="title">Attorney &amp; Counselor at Law</div>
    <div class="concept">Stationery Concept</div>
  </header>

  <!-- business cards -->
  <div class="card card-front" style="left:19px;top:161px">
    <div class="brand-mark"><span class="brand-square"></span><span class="brand-name">Marisol K. Denby</span></div>
  </div>
  <div class="label" style="left:19px;top:229px">Card Front</div>

  <div class="card card-back" style="left:149px;top:161px">
    <div class="person">Marisol K. Denby</div>
    <div class="role">Attorney &amp; Counselor at Law</div>
    <div class="contact">Phone (858) 555-0147<br>Fax (858) 555-0147<br>Email marisol@counseldenby.example</div>
  </div>
  <div class="label" style="left:149px;top:229px">Card Back</div>

  <div class="card card-front gray" style="left:19px;top:249px">
    <div class="brand-mark"><span class="brand-square"></span><span class="brand-name">Marisol K. Denby</span></div>
  </div>
  <div class="label" style="left:19px;top:318px">Card Front Gray</div>

  <div class="card card-back gray" style="left:149px;top:249px">
    <div class="person">Marisol K. Denby</div>
    <div class="role">Attorney &amp; Counselor at Law</div>
    <div class="contact">Phone (858) 555-0147<br>Fax (858) 555-0147<br>Email marisol@counseldenby.example</div>
  </div>
  <div class="label" style="left:149px;top:318px">Card Back Gray</div>

  <!-- letterheads -->
  <div class="letterhead" style="left:329px">
    <div class="head"><div class="brand-mark"><span class="brand-square"></span><span class="brand-name">Marisol K. Denby</span></div></div>
    <div class="address">The Quillgate<br>27815 E. Halvorsen Lane<br>Suite 610<br>San Diego, CA 92984<br>(858) 555-0147</div>
    <div class="foot">www.counseldenby.example</div>
    <div class="band"></div>
  </div>
  <div class="label" style="left:420px;top:350px">Letterhead One</div>

  <div class="letterhead" style="left:588px">
    <div class="head"><div class="brand-mark"><span class="brand-square"></span><span class="brand-name">Marisol K. Denby</span></div></div>
    <div class="foot">www.counseldenby.example</div>
    <div class="band"></div>
  </div>
  <div class="label" style="left:680px;top:350px">Letterhead Two</div>

  <!-- envelopes -->
  <div class="envelope" style="top:29px;background:linear-gradient(180deg,#6a6c6f,var(--gray-dark))">
    <svg width="312" height="108" viewBox="0 0 312 108"><polygon points="0,0 312,0 156,62" fill="#7a7c80"/><polyline points="0,0 156,62 312,0" fill="none" stroke="#55575a" stroke-width="1"/></svg>
    <div class="brand-mark" style="left:118px;top:12px"><span class="brand-square"></span><span class="brand-name" style="color:#fff">Marisol K. Denby</span></div>
  </div>

  <div class="envelope" style="top:132px;background:var(--paper-shade)">
    <svg width="312" height="108" viewBox="0 0 312 108"><defs><linearGradient id="flap" x1="0" y1="0" x2="0" y2="1"><stop offset="0" stop-color="#1c8cc2"/><stop offset="1" stop-color="#0f5f8c"/></linearGradient></defs><polygon points="0,0 312,0 156,58" fill="url(#flap)"/></svg>
    <div class="brand-mark" style="left:118px;top:10px"><span class="brand-square" style="background:#fff"></span><span class="brand-name" style="color:#fff">Marisol K. Denby</span></div>
  </div>

  <div class="envelope" style="top:192px;background:var(--paper)">
    <div class="return">
      <div class="brand-mark"><span class="brand-square"></span><span class="brand-name">Marisol K. Denby</span></div>
      <span>The Quillgate</span><span>27815 E. Halvorsen Lane</span><span>Suite 610</span><span>San Diego, CA 92984</span>
    </div>
    <div class="edge"></div>
  </div>

  <div class="envelope" style="top:240px;background:var(--paper)">
    <div class="return">
      <div class="brand-mark"><span class="brand-square"></span><span class="brand-name">Marisol K. Denby</span></div>
      <span>The Quillgate</span><span>27815 E. Halvorsen Lane</span><span>Suite 610</span><span>San Diego, CA 92984</span>
    </div>
    <div class="edge"></div>
  </div>
  <div class="label" style="left:1000px;top:352px">Envelope Front</div>
  <div class="label" style="left:1120px;top:352px">Envelope Back</div>

</div>
</body>
</html>
```